Business Card Design - Marla_BWT

We need a Business card for a new company based in Sydney Australia.
We distribute children's toys and educational products to Australian retailers.
Our clients are overseas manufacturers, Australian retail shop owners, schools, educational centres.
The design should communicate education and development for children.
The colours should be Australian primary bold colours. Green and Gold is an option to symbolise Australia.

Target Market(s)

Overseas manufacturers, Australian retail shop owners, Trade fairs

Industry/Entity Type

Education

Requirements
Must have
• BUSINESS CARD TO READ:

Marla Tessoway
Managing Director

Tel: +61 452 318 904
Fax: +61 2 9163 2580
Marla@BrightWhirlTots.com.au

Bright Whirl Tots Pty Ltd
4/219 Harwood Pde.
Tarrow Point, Sydney, NSW
Australia, 2093
www.BrightWhirlTots.com.au
Nice to have
• BACK OF THE BUSINESS CARD:

Images:

Greta Hollandier
Rupert Baby Koala Cub
Baby Wenda & Otto

same as business card example uploaded

```html
<!DOCTYPE html>
<html lang="en">
<head>
<meta charset="utf-8">
<title>Bright Whirl Tots – Business Card</title>
<link rel="stylesheet" href="https://fonts.googleapis.com/css2?family=Questrial&display=swap">
<style>
  :root {
    --bg: #2b2b2b;
    --card-white: #ffffff;
    --green-deep: #8fae1f;
    --green-light: #c3d64a;
    --gold: #f4d800;
    --gold-soft: #fbe96a;
    --ink: #1a1a1a;
    --brand-blue: #1f44d6;
    --brand-dot: #8e98c8;
    --band: rgba(255, 255, 255, 0.38);
    --plush-brown: #a9794a;
    --plush-light: #e6d2b0;
  }
  * { margin: 0; padding: 0; box-sizing: border-box; }
  html, body { width: 800px; height: 1200px; overflow: hidden; }
  body {
    background: var(--bg);
    font-family: "Questrial", "Century Gothic", sans-serif;
    color: var(--ink);
    position: relative;
  }
  .card {
    position: absolute;
    left: 110px;
    width: 560px;
    height: 336px;
    overflow: hidden;
  }
  .card--front {
    top: 165px;
    background:
      radial-gradient(circle at 450px 70px, var(--gold) 0, var(--gold) 150px, var(--gold-soft) 152px, rgba(244,216,0,0) 240px),
      linear-gradient(120deg, var(--green-deep) 0%, var(--green-light) 55%, #dfe77a 100%);
  }
  .card--back {
    top: 652px;
    background: var(--card-white);
  }
  .plush-photo {
    position: absolute;
    border-radius: 40px;
  }
  .card--front .plush-photo {
    left: 45px; top: 40px; width: 290px; height: 268px;
    background: radial-gradient(ellipse at 45% 45%, #c9956a 0%, var(--plush-brown) 55%, rgba(169,121,74,0) 75%);
  }
  .card--back .plush-photo {
    left: 148px; top: 18px; width: 380px; height: 318px;
    background: radial-gradient(ellipse at 55% 50%, var(--plush-light) 0%, #d8bd92 50%, rgba(216,189,146,0) 75%);
  }
  .brand {
    position: absolute;
    display: flex;
    flex-direction: column;
    align-items: flex-end;
  }
  .brand__row { display: flex; align-items: center; gap: 8px; }
  .brand__dot { border-radius: 50%; background: var(--brand-dot); flex: none; }
  .brand__name { color: var(--brand-blue); font-weight: 400; white-space: nowrap; }
  .brand__tag { color: var(--ink); white-space: nowrap; }
  .card--front .brand { right: 24px; top: 30px; }
  .card--front .brand__dot { width: 34px; height: 34px; }
  .card--front .brand__name { font-size: 27px; }
  .card--front .brand__tag { font-size: 12px; margin-top: 4px; }
  .card--back .brand { left: 32px; top: 114px; align-items: flex-start; }
  .card--back .brand__dot { width: 24px; height: 24px; }
  .card--back .brand__name { font-size: 18px; }
  .card--back .brand__tag { font-size: 8px; margin-top: 3px; margin-left: 58px; }
  .contact {
    position: absolute;
    right: 24px;
    top: 132px;
    text-align: right;
    font-size: 12.5px;
    line-height: 16px;
  }
  .contact__name { font-size: 20px; line-height: 26px; margin-bottom: 4px; }
  .contact__title { font-size: 13px; margin-bottom: 4px; }
  .address-band {
    position: absolute;
    left: 0; right: 0; top: 250px; bottom: 0;
    background: var(--band);
  }
  .address {
    position: absolute;
    right: 24px;
    top: 256px;
    text-align: right;
    font-size: 12.5px;
    line-height: 15.5px;
  }
</style>
</head>
<body>
  <section class="card card--front">
    <div class="plush-photo" role="img" aria-label="Photo of a brown plush teddy bear sitting"></div>
    <div class="brand">
      <div class="brand__row">
        <span class="brand__dot"></span>
        <span class="brand__name">Bright Whirl Tots</span>
      </div>
      <span class="brand__tag">Australian Distributor</span>
    </div>
    <div class="contact">
      <p class="contact__name">Marla Tessoway</p>
      <p class="contact__title">Managing Director</p>
      <p>Tel: +61 452 318 904</p>
      <p>Fax: +61 2 9163 2580</p>
      <p>Marla@BrightWhirlTots.com.au</p>
    </div>
    <div class="address-band"></div>
    <address class="address" style="font-style:normal">
      <p>Bright Whirl Tots Pty Ltd</p>
      <p>4/219 Harwood Pde.</p>
      <p>Tarrow Point, Sydney, NSW</p>
      <p>Australia, 2093</p>
      <p>www.BrightWhirlTots.com.au</p>
    </address>
  </section>

  <section class="card card--back">
    <div class="brand">
      <div class="brand__row">
        <span class="brand__dot"></span>
        <span class="brand__name">Bright Whirl Tots</span>
      </div>
      <span class="brand__tag">Australian Distributor</span>
    </div>
    <div class="plush-photo" role="img" aria-label="Photo of three plush teddy bears sitting together"></div>
  </section>
</body>
</html>
```